Redesign for luxury lifestyle PR agency

Ginger Kite Otter is a luxury lifestyle public relations agency specialising in indigenous and regenerative travel. We are the elephant you want in the room. We represent interesting brands and people who would be described as changemakers in their respective fields. The winning design should be stylish, clean cut and earthy. It should communicate that Ginger Kite Otter is professional and representative of the industries that it serves. The purpose of the website is to provide clear information to potential customers and media, improve the image and brand of the company, position the company as one of scale and increase sales conversions. Its aesthetic will be aspirational and image led in an editorial style. I would like to be able to easily edit the website once finished and be able to work with the designer on an ad hoc basis once the project is completed.

Please see below for some website I like the style of:

https://www.velmora-ensemble.com/

https://www.tasbergglobal.com/

https://www.brindlequarterly.co.uk/

Pages I would like to include are:

Home
Services
Clients
Testimonials
About Us
News

I'm also attaching a proposal that I really liked the style of and I would like this sort of aesthetic on the website too. My logo is also attached (it is likely that the colour palette might change with the website).

I'm open to inspiration on the colours - my immediate preference is greens and/or blues.

Here is the existing website that I built myself on Wix - https://www.gingerkiteotter.com/ (it looks so outdated and amateur now hence the need of a serious rebrand)

Target Market(s)

Luxury travel and lifestyle brands

Industry/Entity Type

Luxury travel and lifestyle

Number of Pages Required

1 page

Font styles to use
Serif
Other font styles liked:
• Open to suggestions

Requirements
Must have
• Beautiful imagery

```html
<!DOCTYPE html>
<html lang="en">
<head>
<meta charset="utf-8">
<title>Ginger Kite Otter — Lifestyle PR</title>
<link rel="stylesheet" href="https://fonts.googleapis.com/css2?family=Gilda+Display&family=Jost:ital,wght@0,300;0,400;0,500;0,600;1,300;1,400&display=swap">
<style>
:root{
  --blue:#0a9ee0;
  --green:#86c43b;
  --navy:#2b2d7c;
  --ink:#1b1b1f;
  --grey:#55565c;
  --footer:#0b0d1f;
  --mist:#e9f0f8;
  --white:#ffffff;
}
*{margin:0;padding:0;box-sizing:border-box}
html,body{width:1200px;height:4054px;overflow:hidden;background:var(--white)}
body{position:relative;font-family:"Jost",sans-serif;color:var(--ink)}
.abs{position:absolute}
.serif{font-family:"Gilda Display",serif;font-weight:400}
.photo{position:absolute}
.btn{position:absolute;display:flex;align-items:center;justify-content:center;color:var(--white);font-size:12.5px;font-weight:400;text-decoration:none}
.btn-blue{background:var(--blue)}
.btn-green{background:var(--green)}

/* header */
.site-header{position:absolute;left:0;top:0;width:1200px;height:74px;background:var(--white);z-index:3}
.brand-badge{position:absolute;left:196px;top:-20px;width:110px;height:112px;border-radius:50%;background:var(--white);z-index:4;display:flex;flex-direction:column;align-items:center;justify-content:center;padding-top:22px}
.brand-badge .dot{width:22px;height:22px;border-radius:50%;background:var(--blue);margin-bottom:4px}
.brand-badge .name{font-size:12px;line-height:13px;color:var(--blue);text-align:center;font-weight:400;letter-spacing:.5px}
.main-nav a{position:absolute;top:28px;font-size:12.5px;color:var(--navy);text-decoration:none}
.main-nav a.active{color:var(--blue)}
.nav-cta{left:887px;top:19px;width:112px;height:36px}

/* hero */
.hero{left:0;top:74px;width:1200px;height:406px;background:linear-gradient(180deg,#cfe0e6 0%,#a9c9d4 45%,#3f8aa3 65%,#2d6f8c 100%)}
.hero-title{left:203px;top:440px;font-size:58px;color:var(--ink);z-index:2}
.rule-v{position:absolute;width:2px;background:var(--ink)}
.intro-lead{left:406px;top:562px;width:600px;font-size:20px;line-height:30px;color:var(--navy);font-weight:400}
.intro-rule{left:406px;top:664px;width:62px;height:2px;background:var(--blue)}
.intro-body{left:531px;top:656px;width:455px;font-size:11.5px;line-height:18.5px;color:var(--grey);font-weight:300}

/* testimonials */
.testimonial-bg{left:94px;top:858px;width:1012px;height:470px;background:linear-gradient(135deg,#3a3634 0%,#4b4541 40%,#5c4234 70%,#3a2a22 100%);clip-path:polygon(106px 0,1012px 0,1012px 282px,906px 282px,906px 470px,0 470px,0 282px,106px 282px)}
.testimonial-title{left:0;width:1200px;top:900px;text-align:center;font-size:44px;color:var(--white)}
.quote-text{left:320px;top:1023px;width:560px;text-align:center;font-size:14.5px;line-height:19px;font-style:italic;font-weight:300;color:#eeeeee}
.avatar{left:573px;top:1124px;width:54px;height:54px;border-radius:50%;background:#c9c2bb;border:2px solid #fff}
.client-name{left:0;width:1200px;top:1189px;text-align:center;font-size:12px;font-weight:600;color:var(--white)}
.client-role{left:0;width:1200px;top:1207px;text-align:center;font-size:9.5px;color:#dddddd}

/* services */
.section-title{left:0;width:1200px;text-align:center;font-size:44px;color:var(--ink)}
.service{position:absolute;left:613px;width:400px}
.service .bar{width:62px;height:2px;background:var(--ink)}
.service h3{font-family:"Gilda Display",serif;font-weight:400;font-size:19px;margin-top:12px;color:var(--ink)}
.service h3.highlight{color:var(--navy)}
.service p{font-size:10.5px;line-height:15px;color:var(--grey);margin-top:10px;font-weight:300}

/* clients */
.clients-band{left:0;top:2120px;width:1106px;height:288px;background:var(--green)}
.clients-title{left:200px;top:2174px;font-size:46px;color:var(--white)}
.clients-sub{left:200px;top:2235px;width:600px;font-size:18.5px;line-height:22px;color:var(--white);font-weight:300}

/* articles */
.article{position:absolute}
.article .date{font-size:10px;color:var(--blue)}
.article h4{font-family:"Gilda Display",serif;font-weight:400;font-size:13.5px;line-height:19px;color:var(--navy);margin-top:6px}
.article p{font-size:9.5px;line-height:15px;color:var(--grey);margin-top:9px;font-weight:300}
.article .more{display:block;font-family:"Gilda Display",serif;font-size:12px;color:var(--blue);margin-top:16px;text-decoration:none}
.article-card{left:455px;top:3170px;width:288px;height:169px;background:var(--white);padding:18px 24px 0 24px}

/* newsletter */
.newsletter-bg{left:94px;top:3496px;width:1106px;height:262px;background:var(--mist)}
.newsletter-title{left:200px;top:3466px;font-size:46px;color:var(--ink)}
.newsletter-text{left:406px;top:3560px;width:620px;font-size:19px;line-height:29px;color:var(--ink);font-weight:300}
.email-field{left:294px;top:3655px;width:500px;height:37px;border:1px solid var(--navy);background:var(--white);font-size:10px;color:var(--grey);padding:11px 14px;font-family:"Jost",sans-serif}
.submit{left:806px;top:3655px;width:100px;height:37px;background:var(--navy)}

/* footer */
.site-footer{left:0;top:3758px;width:1200px;height:296px;background:var(--footer);color:var(--white)}
.footer-brand{position:absolute;left:198px;top:66px;width:150px;text-align:center}
.footer-brand .dot{width:46px;height:46px;border-radius:50%;background:var(--blue);margin:0 auto 10px}
.footer-brand .name{font-size:24px;line-height:26px;color:var(--blue);font-weight:400}
.footer-heading{position:absolute;font-family:"Gilda Display",serif;font-size:17px;color:var(--white)}
.contact-line{position:absolute;left:438px;display:flex;align-items:flex-start;gap:10px;font-size:11px;color:#e5e5e5;font-weight:300}
.contact-line.big{font-size:15px}
.quick-links a{position:absolute;font-size:10px;color:#e5e5e5;text-decoration:none;font-weight:300}
.social{position:absolute;left:969px;width:30px;height:30px;border-radius:50%}
.footer-rule{left:94px;top:228px;width:1012px;height:1px;background:#2a2d44}
.copyright{left:0;width:1200px;top:256px;text-align:center;font-size:10px;color:#d6d6d6;font-weight:300}
.copyright span{color:var(--blue)}
</style>
</head>
<body>

<header class="site-header">
  <div class="brand-badge"><div class="dot"></div><div class="name">GINGER KITE<br>OTTER</div></div>
  <nav class="main-nav">
    <a class="active" style="left:452px">Home</a>
    <a style="left:510px">About Us</a>
    <a style="left:587px">Services</a>
    <a style="left:662px">Clients</a>
    <a style="left:726px">Testimonials</a>
    <a style="left:824px">News</a>
  </nav>
  <a class="btn btn-green nav-cta">Contact Us</a>
</header>

<div class="photo abs hero" role="img" aria-label="Rocky wooded islet in a turquoise sea reached by a rope bridge"></div>
<h1 class="abs serif hero-title">Who We Are</h1>
<div class="rule-v" style="left:1104px;top:446px;height:71px"></div>

<section class="about">
  <p class="abs intro-lead">Ginger Kite Otter is a boutique lifestyle PR and communications agency helping brands get their voices heard in the UK.</p>
  <div class="abs intro-rule"></div>
  <p class="abs intro-body">It is a long established fact that a reader will be distracted by the readable content of a page when looking at its layout. The point of using Lorem Ipsum is that it has a more-or-less normal distribution of letters, as opposed to using 'Content here, content here', making it look like readable English ...</p>
  <a class="btn btn-blue" style="left:532px;top:759px;width:125px;height:38px">Discover More</a>
</section>

<section class="testimonials">
  <div class="photo abs testimonial-bg" role="img" aria-label="Warm open-plan living room with armchair, wooden floor and plants, dimmed"></div>
  <h2 class="abs serif testimonial-title">Happy Clients Say</h2>
  <svg class="abs" style="left:580px;top:978px" width="40" height="24" viewBox="0 0 40 24">
    <g fill="var(--green)"><circle cx="9" cy="15" r="8"/><path d="M1 15 C1 6 6 1 14 0 L14 4 C9 5 7 9 7 13 Z"/><circle cx="29" cy="15" r="8"/><path d="M21 15 C21 6 26 1 34 0 L34 4 C29 5 27 9 27 13 Z"/></g>
  </svg>
  <p class="abs quote-text">Lorem ipsum dolor sit amet, consectetur adipiscing elit. Suspendisse eleifend id metus id fringilla. Phasellus euismod commodo felis, sit amet egestas dui euismod vitae. Aenean venenatis malesuada nisi sit amet that can are amet hendrerit variations of passages.</p>
  <svg class="abs" style="left:538px;top:1145px" width="14" height="12" viewBox="0 0 14 12"><path d="M13 6H2M6 1 1 6l5 5" stroke="#ddd" stroke-width="1.4" fill="none"/></svg>
  <svg class="abs" style="left:648px;top:1145px" width="14" height="12" viewBox="0 0 14 12"><path d="M1 6h11M8 1l5 5-5 5" stroke="var(--blue)" stroke-width="1.4" fill="none"/></svg>
  <div class="abs avatar" role="img" aria-label="Client portrait"></div>
  <div class="abs client-name">Marcus Delany</div>
  <div class="abs client-role">Happy Client</div>
  <a class="btn btn-green" style="left:550px;top:1241px;width:99px;height:36px">View All</a>
</section>

<section class="services">
  <h2 class="abs serif section-title" style="top:1412px">Our Services</h2>
  <div class="photo abs" style="left:200px;top:1520px;width:324px;height:412px;background:linear-gradient(180deg,#cfe3ee 0%,#8a9a86 30%,#5f6d58 48%,#2fc0bf 52%,#3bbfb8 75%,#6fcfc4 100%)" role="img" aria-label="Boat on a turquoise mountain lake below rocky peaks"></div>
  <div class="service" style="top:1520px"><div class="bar"></div><h3>Strategic Planning</h3><p>It is a long established fact that a reader will be distracted by the readable content of a page when looking at its layout.</p></div>
  <div class="service" style="top:1630px"><div class="bar"></div><h3 class="highlight">Consumer Media Relations</h3><p>It is a long established fact that a reader will be distracted by the readable content of a page when looking at its layout.</p></div>
  <div class="service" style="top:1734px"><div class="bar"></div><h3>Reputation Management</h3><p>It is a long established fact that a reader will be distracted by the readable content of a page when looking at its layout.</p></div>
  <div class="service" style="top:1840px"><div class="bar"></div><h3>Influencer Engagement</h3><p>It is a long established fact that a reader will be distracted by the readable content of a page when looking at its layout.</p></div>
  <div class="service" style="top:1947px"><div class="bar"></div><h3>Creative Consultation</h3><p>It is a long established fact that a reader will be distracted by the readable content of a page when looking at its layout.</p></div>
</section>

<section class="clients">
  <div class="abs clients-band"></div>
  <h2 class="abs serif clients-title">Clients</h2>
  <p class="abs clients-sub">A dynamic collection of innovative lifestyle clients that we are wholly passionate about</p>
  <div class="photo abs" style="left:94px;top:2358px;width:493px;height:312px;background:linear-gradient(180deg,#e6e6e3 0%,#d8d6d0 55%,#b9b1a4 80%,#8a7a66 100%)" role="img" aria-label="Bright living room with cream sofa and wall decor"></div>
  <div class="photo abs" style="left:613px;top:2304px;width:293px;height:281px;background:linear-gradient(180deg,#dfe4e6 0%,#5a7048 35%,#4d5e43 60%,#d9d3c8 85%,#ece8e0 100%)" role="img" aria-label="Garden with palm trees, sculpture and a long water channel"></div>
  <div class="photo abs" style="left:613px;top:2610px;width:493px;height:193px;background:linear-gradient(180deg,#cfd2d0 0%,#9aa29a 40%,#7a6a3e 62%,#5f6a3c 80%,#4c5a2f 100%)" role="img" aria-label="Autumn countryside with poplar trees and a stone manor"></div>
  <a class="btn btn-blue" style="left:277px;top:2720px;width:126px;height:36px">View All Clients</a>
</section>

<section class="articles">
  <h2 class="abs serif section-title" style="top:2856px">Latest Articles</h2>

  <div class="photo abs" style="left:200px;top:2962px;width:181px;height:182px;background:linear-gradient(180deg,#c9d6db 0%,#7f9a8f 45%,#4f7f86 60%,#7a4d2c 80%,#a0693c 100%)" role="img" aria-label="Wooden boat bow on a green mountain lake"></div>
  <div class="article" style="left:200px;top:3160px;width:186px">
    <div class="date">14 Jun, 2022</div>
    <h4>Lorem Ipsum simply dummy text of the printing</h4>
    <p>Lorem Ipsum is simply work text kdummy of work the printing and typesetting industry lorem Ipsum has standard ...</p>
    <a class="more">Read More →</a>
  </div>

  <div class="photo abs" style="left:432px;top:2931px;width:338px;height:288px;background:linear-gradient(180deg,#d8d4cf 0%,#efeeeb 40%,#c9a57e 75%,#8a5a35 100%)" role="img" aria-label="Pour-over coffee being brewed through a paper filter"></div>
  <div class="article article-card">
    <div class="date">20 May, 2022</div>
    <h4>Lorem Ipsum is simply dummy text of the printing and typesetting</h4>
    <p>Lorem Ipsum is simply work text kdummy of work the printing and typesetting industry lorem Ipsum has standard ...</p>
    <a class="more">Read More →</a>
  </div>

  <div class="photo abs" style="left:819px;top:2962px;width:181px;height:182px;background:linear-gradient(180deg,#c5ccd2 0%,#8e979e 35%,#6c8a4f 65%,#5d7a3f 100%)" role="img" aria-label="Hikers with backpacks on a mountain trail"></div>
  <div class="article" style="left:819px;top:3160px;width:186px">
    <div class="date">14 April, 2022</div>
    <h4>Lorem Ipsum simply dummy text of the printing</h4>
    <p>Lorem Ipsum is simply work text kdummy of work the printing and typesetting industry lorem Ipsum has standard ...</p>
    <a class="more">Read More →</a>
  </div>

  <a class="btn btn-green" style="left:539px;top:3359px;width:124px;height:36px">View All News</a>
</section>

<section class="newsletter">
  <div class="abs newsletter-bg"></div>
  <h2 class="abs serif newsletter-title">Subscribe Newsletter</h2>
  <div class="rule-v" style="left:1104px;top:3459px;height:74px;background:var(--green)"></div>
  <p class="abs newsletter-text">Lorem Ipsum is dummy text of the printing and typesetting industry. lorem Ipsum has been industry's standard!</p>
  <div class="abs email-field">Enter Your Email ...</div>
  <a class="btn submit">Submit</a>
</section>

<footer class="abs site-footer">
  <div class="footer-brand"><div class="dot"></div><div class="name">GINGER KITE OTTER</div></div>

  <h5 class="footer-heading" style="left:438px;top:76px">Contact Us</h5>
  <div class="contact-line big" style="top:110px">
    <svg width="12" height="12" viewBox="0 0 12 12" style="margin-top:4px"><path d="M2.5 1 4.5 3.5 3.4 5a7 7 0 0 0 3.6 3.6L8.5 7.5 11 9.5 9.8 11C5 11 1 7 1 2.2Z" fill="none" stroke="var(--green)" stroke-width="1.1"/></svg>
    <span>+44 (0) 7700 900418</span></div>
  <div class="contact-line" style="top:143px">
    <svg width="12" height="10" viewBox="0 0 12 10" style="margin-top:2px"><rect x="0.6" y="0.6" width="10.8" height="8.8" fill="none" stroke="var(--green)" stroke-width="1.1"/><path d="M.6.8 6 5.5 11.4.8" fill="none" stroke="var(--green)" stroke-width="1.1"/></svg>
    <span>hello@gingerkiteotter.com</span></div>
  <div class="contact-line" style="top:174px;font-size:10px;line-height:14px">
    <svg width="10" height="13" viewBox="0 0 10 13" style="margin-top:1px"><path d="M5 12S1 7.5 1 4.8a4 4 0 0 1 8 0C9 7.5 5 12 5 12Z" fill="none" stroke="var(--green)" stroke-width="1.1"/><circle cx="5" cy="4.8" r="1.4" fill="var(--green)"/></svg>
    <span>48 Larkspur Row, Fenwick Vale,<br>FV 20914</span></div>

  <h5 class="footer-heading" style="left:750px;top:75px">Quick Links</h5>
  <nav class="quick-links">
    <a style="left:750px;top:114px">Home</a>
    <a style="left:750px;top:133px">About Us</a>
    <a style="left:750px;top:152px">Services</a>
    <a style="left:750px;top:171px">Clients</a>
    <a style="left:750px;top:190px">Testimonials</a>
    <a style="left:839px;top:114px">News</a>
    <a style="left:839px;top:133px">Contact Us</a>
  </nav>

  <span class="social" style="top:79px;background:var(--blue)"></span>
  <span class="social" style="top:117px;background:var(--green)"></span>
  <span class="social" style="top:155px;background:var(--blue)"></span>

  <div class="abs footer-rule"></div>
  <p class="abs copyright">© 2022 <span>Ginger Kite Otter</span> - All Rights Reserved</p>
</footer>

</body>
</html>
```